Water Filtration Company needs a business card design using our existing logo/colours!

We design and manufacture and export specialised water filtration equipment. Our equipment will take unclean dirty water and filters to safe clean drinkable water.
We would like to see designs using our existing logo and colours (see attached "Palette") that represents clean safe drinking water (fresh, clean designs but still professional and modern). Our customers are other businesses who supply water filtration equipment, governments, and private individuals.
BUSINESS CARD DETAILS (Common details):
Tel: + 61 7 55 419 276
www: brindlepeak.com.au
Address: 3/47 Cordwell Parade
Marlow Flats NSW 2593 Australia
(please include the word Australia as we are an international company)
Must include: COMMERCIAL WATER FILTRATION EQUIPMENT
NAME NO 1:
Owen Pritch
General Manager
Mobile: +61 427 38 91 04
Email: owen@brindlepeak.com.au
NAME NO. 2:
Gina Rosk
Business Manager
Mobile: +61 409 572 148
Email: gina@brindlepeak.com.au
Must Have:
1) PRINT READY IN .AI & .PDF FORMATS
2) Also saved in file format .ai (Adobe Illustrator - compatible with CS4)
3) Use existing LOGO & COLOURS: Please use our logo (see attached file)
4) FONTS: we have used Avenir & Helvetica in the past but are open to other font types for the address etc.
Thank you!

```html
<!DOCTYPE html>
<html lang="en">
<head>
<meta charset="utf-8">
<title>Brindle Peak – Business Cards</title>
<link rel="stylesheet" href="https://fonts.googleapis.com/css2?family=Mulish:wght@400;600&display=swap">
<style>
  :root {
    --bg: #e9ecee;
    --card: #ffffff;
    --deep: #0b4f82;
    --teal: #2ab3c4;
    --ink-teal: #1b8ea3;
    --ink-soft: #3f96a8;
    --ink-dark: #123f63;
    --rule: #0f5c8c;
  }
  * { box-sizing: border-box; margin: 0; padding: 0; }
  html, body { width: 1200px; height: 939px; overflow: hidden; }
  body {
    background: var(--bg);
    font-family: "Mulish", "Avenir", "Helvetica", sans-serif;
    position: relative;
  }
  .card {
    position: absolute;
    top: 315px;
    width: 540px;
    height: 309px;
    background: var(--card);
    box-shadow: 0 6px 18px rgba(0,0,0,.12);
    overflow: hidden;
  }
  .card--front { left: 40px; }
  .card--back { left: 620px; }
  .wave { position: absolute; left: 0; top: 0; width: 540px; height: 40px; }

  .brand {
    position: absolute;
    display: flex;
    align-items: center;
    font-weight: 600;
    letter-spacing: .5px;
  }
  .brand__name { font-size: 22px; color: var(--ink-teal); }
  .brand__bar {
    width: 72px; height: 30px; margin-left: 14px;
    background: linear-gradient(90deg, var(--teal), var(--deep));
  }
  .card--front .brand { right: 0; top: 62px; }

  .person { position: absolute; color: var(--ink-teal); }
  .person--one { left: 40px; top: 62px; }
  .person--two { left: 300px; top: 150px; }
  .person__name { font-size: 27px; font-weight: 400; line-height: 1.1; }
  .person__role { font-size: 11px; color: var(--ink-soft); margin: 4px 0 14px 56px; }
  .contact { list-style: none; font-size: 11px; color: var(--ink-teal); }
  .contact li { display: flex; align-items: center; gap: 10px; margin-bottom: 9px; }
  .contact svg { width: 14px; height: 14px; flex: none; }

  .divider {
    position: absolute; left: 262px; top: 150px;
    width: 1.5px; height: 56px; background: var(--rule);
  }

  .details { position: absolute; left: 34px; top: 54px; }
  .details .contact li { margin-bottom: 6px; font-size: 12px; }
  .details .contact .addr { align-items: flex-start; }
  .details .contact .addr span { line-height: 1.35; }
  .tagline {
    margin-top: 12px;
    font-size: 14px;
    font-weight: 600;
    color: var(--ink-dark);
    letter-spacing: .3px;
  }
  .brand-block {
    position: absolute; right: 0; top: 148px;
    width: 170px; height: 52px;
    display: flex; align-items: center; justify-content: center;
    background: linear-gradient(90deg, var(--teal), var(--deep));
  }
  .brand-block .brand__name { color: #ffffff; font-weight: 600; font-size: 20px; }
</style>
</head>
<body>
  <svg width="0" height="0" style="position:absolute">
    <defs>
      <linearGradient id="waveFill" x1="0" x2="1" y1="0" y2="0">
        <stop offset="0" stop-color="#0b4f82"/>
        <stop offset="1" stop-color="#2ab3c4"/>
      </linearGradient>
    </defs>
  </svg>

  <!-- Front: two staff contacts -->
  <section class="card card--front">
    <svg class="wave" viewBox="0 0 540 40" preserveAspectRatio="none" aria-hidden="true">
      <path d="M0 0 H540 V2 C420 2 360 6 260 14 C170 22 80 26 0 26 Z" fill="url(#waveFill)"/>
    </svg>

    <div class="person person--one">
      <h2 class="person__name">Owen Pritch</h2>
      <p class="person__role">General Manager</p>
      <ul class="contact">
        <li><svg viewBox="0 0 14 14"><rect x="3" y="0.5" width="8" height="13" rx="1.5" fill="none" stroke="#1b8ea3" stroke-width="1.3"/><rect x="4.5" y="2.5" width="5" height="6" fill="#1b8ea3"/></svg><span>+61 427 38 91 04</span></li>
        <li><svg viewBox="0 0 14 14"><rect x="0.7" y="2.5" width="12.6" height="9" fill="none" stroke="#1b8ea3" stroke-width="1.3"/><path d="M1 3 L7 8 L13 3" fill="none" stroke="#1b8ea3" stroke-width="1.3"/></svg><span>owen@brindlepeak.com.au</span></li>
      </ul>
    </div>

    <span class="divider"></span>

    <div class="brand">
      <span class="brand__name">brindle peak</span>
      <span class="brand__bar"></span>
    </div>

    <div class="person person--two">
      <h2 class="person__name">Gina Rosk</h2>
      <p class="person__role">Business Manager</p>
      <ul class="contact">
        <li><svg viewBox="0 0 14 14"><rect x="3" y="0.5" width="8" height="13" rx="1.5" fill="none" stroke="#1b8ea3" stroke-width="1.3"/><rect x="4.5" y="2.5" width="5" height="6" fill="#1b8ea3"/></svg><span>+61 409 572 148</span></li>
        <li><svg viewBox="0 0 14 14"><rect x="0.7" y="2.5" width="12.6" height="9" fill="none" stroke="#1b8ea3" stroke-width="1.3"/><path d="M1 3 L7 8 L13 3" fill="none" stroke="#1b8ea3" stroke-width="1.3"/></svg><span>gina@brindlepeak.com.au</span></li>
      </ul>
    </div>
  </section>

  <!-- Back: company details -->
  <section class="card card--back">
    <svg class="wave" viewBox="0 0 540 40" preserveAspectRatio="none" aria-hidden="true">
      <path d="M0 0 H540 V2 C420 2 360 6 260 14 C170 22 80 26 0 26 Z" fill="url(#waveFill)"/>
    </svg>

    <div class="details">
      <ul class="contact">
        <li><svg viewBox="0 0 14 14"><path d="M3 1 L5.5 1 L6.5 4 L5 5.2 C5.8 7 7 8.2 8.8 9 L10 7.5 L13 8.5 L13 11 C13 12 12 13 11 13 C5.5 12.5 1.5 8.5 1 3 C1 2 2 1 3 1 Z" fill="#1b8ea3"/></svg><span>+ 61 7 55 419 276</span></li>
        <li><svg viewBox="0 0 14 14"><circle cx="7" cy="7" r="6" fill="none" stroke="#1b8ea3" stroke-width="1.3"/><ellipse cx="7" cy="7" rx="2.6" ry="6" fill="none" stroke="#1b8ea3" stroke-width="1.1"/><path d="M1 7 H13" stroke="#1b8ea3" stroke-width="1.1"/></svg><span>brindlepeak.com.au</span></li>
        <li class="addr"><svg viewBox="0 0 14 14"><path d="M7 13 C4 9 2.5 7 2.5 5 A4.5 4.5 0 0 1 11.5 5 C11.5 7 10 9 7 13 Z" fill="#1b8ea3"/><circle cx="7" cy="5" r="1.6" fill="#fff"/></svg><span>3/47 Cordwell Parade<br>Marlow Flats NSW 2593 Australia</span></li>
      </ul>
      <p class="tagline">COMMERCIAL WATER FILTRATION EQUIPMENT</p>
    </div>

    <div class="brand-block">
      <span class="brand__name">brindle peak</span>
    </div>
  </section>
</body>
</html>
```